TIDAL VERGE needs bisness cards pronto

Bisness name is "TIDAL VERGE" new bisness the bisness includes lawn mowing, garden matanace, and any jobs around the house.
I need a card that is colorful and vibrant and the bisness of lawn mowing maybe with some nature with it. It also needs my contact details"Darren Quellby mobile 0413562049 call for free quote and email norma.vance@fernmail.com.au and a catchy tag line

Industry/Entity Type

House

Requirements
Must have
• Bisness name "TIDAL VERGE"
Contact details "0413562049"
Email norma.vance@fernmail.com.au
Call for free quote

```html
<!DOCTYPE html>
<html lang="en">
<head>
<meta charset="utf-8">
<title>Tidal Verge – Business Cards</title>
<link rel="stylesheet" href="https://fonts.googleapis.com/css2?family=Questrial&family=Arimo:wght@400;700&display=swap">
<style>
  :root {
    --canvas-bg: #e9ebee;
    --card-shadow: rgba(20, 30, 50, 0.22);
    --front-glow: #2ba4dc;
    --front-mid: #1f78c0;
    --front-edge: #18549e;
    --front-text: #ffffff;
    --front-tagline: #d8ecfb;
    --back-bg: #ffffff;
    --back-name: #4a4a4a;
    --back-detail: #555555;
    --brand-blue: #3a5bb0;
    --quote-red: #e8202a;
    --divider: #8a8a8a;
  }

  html, body {
    margin: 0;
    padding: 0;
    width: 1200px;
    height: 900px;
    overflow: hidden;
    background: var(--canvas-bg);
  }

  .canvas {
    width: 1200px;
    height: 900px;
    display: flex;
    flex-direction: column;
    align-items: center;
    justify-content: center;
    gap: 60px;
  }

  .card {
    position: relative;
    width: 620px;
    height: 354px;
    box-sizing: border-box;
    box-shadow: 0 10px 28px var(--card-shadow);
  }

  /* Front side */
  .card--front {
    background: radial-gradient(ellipse at 50% 42%, var(--front-glow) 0%, var(--front-mid) 48%, var(--front-edge) 100%);
    display: flex;
    flex-direction: column;
    align-items: center;
    justify-content: center;
  }

  .front__brand {
    font-family: "Questrial", sans-serif;
    font-size: 54px;
    letter-spacing: 2px;
    color: var(--front-text);
    margin: 0;
    margin-top: -20px;
  }

  .front__tagline {
    position: absolute;
    bottom: 26px;
    left: 0;
    right: 0;
    text-align: center;
    font-family: "Questrial", sans-serif;
    font-size: 17px;
    letter-spacing: 0.5px;
    color: var(--front-tagline);
    margin: 0;
  }

  /* Back side */
  .card--back {
    background: var(--back-bg);
  }

  .back__name {
    position: absolute;
    left: 44px;
    top: 48px;
    margin: 0;
    font-family: "Arimo", sans-serif;
    font-weight: 400;
    font-size: 31px;
    color: var(--back-name);
  }

  .back__brand {
    position: absolute;
    right: 36px;
    top: 112px;
    margin: 0;
    font-family: "Questrial", sans-serif;
    font-size: 26px;
    letter-spacing: 1.5px;
    color: var(--brand-blue);
  }

  .back__cta {
    position: absolute;
    left: 44px;
    top: 196px;
    margin: 0;
    font-family: "Arimo", sans-serif;
    font-weight: 700;
    font-size: 18px;
    color: var(--quote-red);
  }

  .back__divider {
    position: absolute;
    left: 244px;
    top: 176px;
    width: 1px;
    height: 76px;
    background: var(--divider);
  }

  .back__contact {
    position: absolute;
    left: 264px;
    top: 196px;
    margin: 0;
    font-family: "Arimo", sans-serif;
    font-size: 16px;
    line-height: 24px;
    color: var(--back-detail);
    font-style: normal;
  }
</style>
</head>
<body>
  <main class="canvas">
    <section class="card card--front" aria-label="Business card front">
      <h1 class="front__brand">TIDAL VERGE</h1>
      <p class="front__tagline">Lawn Mowing, Garden Maintenance &amp; Much More</p>
    </section>

    <section class="card card--back" aria-label="Business card back">
      <h2 class="back__name">Darren Quellby</h2>
      <p class="back__brand">TIDAL VERGE</p>
      <p class="back__cta">Call for Free Quote</p>
      <div class="back__divider"></div>
      <address class="back__contact">
        M: 0413562049<br>
        E: norma.vance@fernmail.com.au
      </address>
    </section>
  </main>
</body>
</html>
```